Lumo Organic Baby Wipes for retail sales into supermarkets

Design a new Organic Baby Wipes Pack that has a similar feel and details to the attachments under the Brand Name LUMO Organics. Please keep all writing in English and highlight the following info on the Pack. - 80 Pack, 100% Biodegradable,
Aloe Vera, Chamomile,Natural Vitamin E to soothe baby's skin.
Hypo Allergenic, pH Balanced for baby's skin.
Fragrance Free, Alcohol Free, Chlorine Free, Parabens Free.

Target Market(s)

Mums looking for a Organic Baby Wipe

Industry/Entity Type

Baby

Font styles to use
Sans Serif

Colors
9bcb3c
abd036
cadf82
ffffff

Requirements
Must have
• Lumo Organics, White Base, majority green writing with different shades, touches of Brown to represent Bamboo Wipes.
• Please make ORGANIC writing very big.
Nice to have
• Natural Organic feel going to use matt packaging.
Should not have
• Cluttered too much information

```html
<!DOCTYPE html>
<html lang="en">
<head>
<meta charset="utf-8">
<title>Lumo Organic Baby Wipes – Pack</title>
<link href="https://fonts.googleapis.com/css2?family=Arvo:wght@700&family=Roboto+Condensed:wght@400&display=swap" rel="stylesheet">
<style>
  :root{
    --bg:#d9f2cf;
    --pack:#ffffff;
    --pack-shade:#f3f6ea;
    --green-leaf:#7ab833;
    --green-lime:#9bcb3c;
    --green-band:#abd036;
    --green-pale:#cadf82;
    --green-deep:#3f6a28;
    --brown:#8a6a2a;
    --brown-light:#b98c3a;
    --ink:#2f3a1c;
    --white:#ffffff;
  }
  *{margin:0;padding:0;box-sizing:border-box}
  html,body{width:1200px;height:1042px;overflow:hidden;background:var(--bg)}
  .canvas{position:relative;width:1200px;height:1042px}
  .pack{position:absolute;left:88px;top:320px;width:1008px;height:470px;
    background:linear-gradient(180deg,var(--pack-shade),var(--pack) 20%,var(--pack) 80%,var(--pack-shade));overflow:hidden}
  .crimp{position:absolute;top:0;width:44px;height:100%;z-index:2;
    background:repeating-linear-gradient(90deg,var(--green-pale) 0 2px,var(--pack-shade) 2px 7px)}
  .crimp--left{left:0}
  .crimp--right{right:0}
  .photo{position:absolute;left:472px;top:16px;width:492px;height:392px;
    background:radial-gradient(ellipse at 40% 45%,#f6d7c6 0%,#efc2ac 45%,#e3ad96 70%,#f4f1ea 100%)}
  .brand{position:absolute;left:122px;top:52px;font:700 72px/1 'Arvo',serif;color:var(--green-leaf)}
  .product-organic{position:absolute;left:56px;top:154px;font:700 52px/1 'Arvo',serif;letter-spacing:3px;
    background:linear-gradient(90deg,var(--brown-light),var(--brown));-webkit-background-clip:text;background-clip:text;color:transparent}
  .product-type{position:absolute;left:66px;top:210px;font:700 44px/1 'Arvo',serif;color:var(--green-deep)}
  .badge{position:absolute;left:372px;top:88px;width:140px;height:150px}
  .benefits{position:absolute;left:44px;top:270px;width:470px;height:138px;
    background:linear-gradient(90deg,var(--green-band) 0%,var(--green-pale) 60%,rgba(202,223,130,0) 100%)}
  .benefits p{position:absolute;left:8px;top:8px;font:400 18px/25px 'Roboto Condensed',sans-serif;color:var(--ink)}
  .seal{position:absolute;left:374px;top:318px;width:78px;height:78px;border:2px solid var(--green-lime);border-radius:50%}
  .tagline-band{position:absolute;right:0;top:414px;width:330px;height:38px;
    background:linear-gradient(90deg,rgba(155,203,60,0),var(--green-lime) 35%,var(--green-leaf))}
  .tagline{position:absolute;right:72px;top:418px;font:400 24px/30px 'Roboto Condensed',sans-serif;color:var(--white)}
</style>
</head>
<body>
<div class="canvas">
  <div class="pack">
    <div class="photo" role="img" aria-label="Photograph of a smiling baby held close by its mother"></div>
    <div class="crimp crimp--left"></div>
    <div class="crimp crimp--right"></div>

    <div class="brand">Lumo</div>
    <div class="product-organic">ORGANIC</div>
    <div class="product-type">Baby Wipes</div>

    <svg class="badge" viewBox="0 0 140 150" aria-label="80 Pack, 100% Biodegradable">
      <defs><path id="badge-arc" d="M18 66 A56 56 0 0 1 128 60"/></defs>
      <text font-family="Arvo, serif" font-weight="700" font-size="22" fill="var(--green-deep)">
        <textPath href="#badge-arc" startOffset="50%" text-anchor="middle">80 ★ Pack</textPath>
      </text>
      <polygon points="72,52 110,74 110,118 72,140 34,118 34,74" fill="var(--green-lime)"/>
      <text x="72" y="104" text-anchor="middle" font-family="Arvo, serif" font-weight="700" font-size="26" fill="var(--white)">100%</text>
      <text x="72" y="122" text-anchor="middle" font-family="Roboto Condensed, sans-serif" font-size="11" fill="var(--white)">Biodegradable</text>
    </svg>

    <div class="benefits">
      <p>Aloe Vera, Chamomile, Natural Vitamin E<br>to soothe baby's skin, Hypo Allergenic,<br>PH Balanced for baby's skin.<br>Fragrance Free, Alcohol Free,<br>Chlorine Free, Parabens Free.</p>
    </div>

    <div class="seal"></div>

    <div class="tagline-band"></div>
    <div class="tagline">Gentle by Nature</div>
  </div>
</div>
</body>
</html>
```